letterhead design using our existing logo

We are a small boutique property management business based in Sydney's Northern Beaches.
We are after a sleek, simple modern letterhead (A4) incorporating our logo and its colours.
Also matching envelope (DL)
I have attached the logo with black text and white text for design options.

Target Market(s)

29-69yo Male and Female

Industry/Entity Type

Property Management

Requirements
Must have
• - Estate Haven logo
• - Address, number and website:
• Suite 7, 18-19 Harlow Parade, Brenton NSW 2187
• Tel: Carl Doyle 0419 267 530 Miriam Kovacs 0407 516 948 www.estatehavenrealty.com.au
Nice to have
• sleek design that looks modern and professional
Should not have
• too many colours or too busy

```html
<!DOCTYPE html>
<html lang="en">
<head>
<meta charset="utf-8">
<title>Estate Haven — Stationery Set</title>
<link href="https://fonts.googleapis.com/css2?family=PT+Sans:wght@400;700&display=swap" rel="stylesheet">
<style>
  :root {
    --backdrop: #e3e3e5;
    --paper: #ffffff;
    --ink: #141718;
    --teal: #1a7a8c;
    --soft-edge: #d6d6d8;
  }
  * { margin: 0; padding: 0; box-sizing: border-box; }
  html, body { width: 1189px; height: 1200px; overflow: hidden; }
  body {
    background: var(--backdrop);
    position: relative;
    font-family: "PT Sans", Arial, sans-serif;
    color: var(--ink);
  }

  .brand {
    display: inline-flex;
    align-items: center;
    gap: 0.3em;
    font-weight: 700;
    text-transform: uppercase;
    letter-spacing: -0.01em;
    white-space: nowrap;
    line-height: 1;
  }
  .brand__mark {
    width: 0.45em;
    height: 0.45em;
    background: var(--teal);
  }
  .brand--dark { color: var(--ink); }
  .brand--light { color: var(--paper); }

  /* Letterhead */
  .letterhead {
    position: absolute;
    left: 50px; top: 99px;
    width: 507px; height: 657px;
    background: var(--paper);
  }
  .letterhead .brand {
    position: absolute;
    left: 18px; top: 62px;
    font-size: 31px;
  }
  .letterhead__contact {
    position: absolute;
    right: 18px; top: 52px;
    text-align: right;
    font-size: 9.5px;
    line-height: 11.5px;
  }
  .contact-line {
    display: flex;
    justify-content: flex-end;
    align-items: center;
    gap: 4px;
  }
  .contact-line svg { width: 10px; height: 10px; }
  .letterhead__address { margin-top: 5px; padding-right: 0; }

  .footer-band {
    position: absolute;
    left: 0; right: 0; bottom: 0;
    background: var(--ink);
  }
  .footer-band__accent {
    position: absolute;
    top: 0; bottom: 0;
    background: var(--teal);
  }
  .letterhead .footer-band { height: 18px; }
  .letterhead .footer-band__accent { left: 37px; width: 116px; }

  /* Folder */
  .folder {
    position: absolute;
    left: 629px; top: 100px;
    width: 506px; height: 653px;
    background: var(--ink);
    display: flex;
    align-items: center;
    justify-content: center;
  }
  .folder .brand { font-size: 37px; margin-top: -80px; }

  /* DL envelope front */
  .envelope-front {
    position: absolute;
    left: 47px; top: 856px;
    width: 401px; height: 201px;
    background: var(--paper);
  }
  .envelope-front .brand {
    position: absolute;
    left: 16px; top: 41px;
    font-size: 17px;
  }
  .envelope-front__address {
    position: absolute;
    left: 16px; top: 163px;
    font-size: 7px;
    line-height: 8.5px;
  }
  .envelope-front .footer-band { height: 11px; }
  .envelope-front .footer-band__accent { left: 29px; width: 92px; }

  /* DL envelope back */
  .envelope-back {
    position: absolute;
    left: 629px; top: 856px;
    width: 402px; height: 201px;
    background: var(--paper);
    border: 1px solid var(--soft-edge);
  }
  .envelope-back__flap {
    position: absolute;
    left: 0; top: 0;
    width: 402px; height: 57px;
  }
  .envelope-back .brand {
    position: absolute;
    left: 50%; top: 22px;
    transform: translateX(-50%);
    font-size: 11.5px;
  }
</style>
</head>
<body>

  <section class="letterhead" aria-label="A4 letterhead">
    <div class="brand brand--dark">Estate Haven<span class="brand__mark"></span></div>
    <div class="letterhead__contact">
      <p class="contact-line">0419 267 530
        <svg viewBox="0 0 10 10" aria-hidden="true"><circle cx="5" cy="5" r="5" fill="#1a7a8c"/><path d="M3 2.6c.4-.3.8-.2 1 .2l.4.8c.1.3 0 .5-.2.7l-.3.2c.3.7.8 1.2 1.5 1.5l.2-.3c.2-.2.4-.3.7-.2l.8.4c.4.2.5.6.2 1l-.4.4C5.2 7.6 2.4 4.8 2.6 3z" fill="#fff"/></svg>
      </p>
      <p class="contact-line">www.estatehavenrealty.com.au
        <svg viewBox="0 0 10 10" aria-hidden="true"><circle cx="5" cy="5" r="5" fill="#1a7a8c"/><rect x="2.5" y="3.2" width="5" height="3.6" fill="none" stroke="#fff" stroke-width="0.8"/><path d="M2.5 3.4 5 5.3 7.5 3.4" fill="none" stroke="#fff" stroke-width="0.8"/></svg>
      </p>
      <p class="letterhead__address">Suite 7, 18-19 Harlow Parade<br>Brenton NSW 2187</p>
    </div>
    <div class="footer-band"><span class="footer-band__accent"></span></div>
  </section>

  <section class="folder" aria-label="Presentation folder cover">
    <div class="brand brand--light">Estate Haven<span class="brand__mark"></span></div>
  </section>

  <section class="envelope-front" aria-label="DL envelope front">
    <div class="brand brand--dark">Estate Haven<span class="brand__mark"></span></div>
    <p class="envelope-front__address">Suite 7, 18-19 Harlow Parade<br>Brenton NSW 2187</p>
    <div class="footer-band"><span class="footer-band__accent"></span></div>
  </section>

  <section class="envelope-back" aria-label="DL envelope back">
    <svg class="envelope-back__flap" viewBox="0 0 402 57" aria-hidden="true">
      <path d="M0 0H402L395 47Q393 55 385 55H17Q9 55 7 47Z" fill="#141718"/>
    </svg>
    <div class="brand brand--light">Estate Haven<span class="brand__mark"></span></div>
  </section>

</body>
</html>
```